Harbor Zentrik needs a new Website Design

We need a WEB site landing page (/template) design, we currently have a company logo.We like the Valtor.com web designEnclosed is our company logo.Our Current website is https://www.harborzentrik.com.au/

1 page

```html
<!DOCTYPE html>
<html lang="en">
<head>
<meta charset="utf-8">
<title>Harbor Zentrik — White-Label Communications</title>
<link href="https://fonts.googleapis.com/css2?family=Roboto:ital,wght@0,300;0,400;0,500;0,700;1,400&display=swap" rel="stylesheet">
<style>
:root{
  --blue:#1e9be0;
  --blue-dark:#1577c4;
  --green:#6cbf3b;
  --ink:#222831;
  --body:#555c66;
  --muted:#9aa0a8;
  --light:#f4f4f4;
  --footer:#1d2733;
  --footer-text:#a8b0ba;
  --white:#ffffff;
  --line:#e3e6ea;
}
*{box-sizing:border-box;margin:0;padding:0}
html,body{width:1200px;height:4874px;overflow:hidden}
body{font-family:"Roboto",Arial,sans-serif;color:var(--body);background:var(--white);position:relative;font-size:13px}
.abs{position:absolute}
a{color:inherit;text-decoration:none}

.hero{position:absolute;left:0;top:0;width:1200px;height:610px;overflow:hidden;
  background:linear-gradient(180deg,#dfeaf4 0%,#cbdcea 55%,#aebfcf 100%)}
.hero-city{position:absolute;left:0;bottom:0;width:1200px;height:150px;background:linear-gradient(180deg,rgba(160,178,196,0) 0%,#9fb0c2 100%)}
.hero-person{position:absolute;left:690px;top:60px;width:330px;height:550px;border-radius:160px 160px 0 0;
  background:linear-gradient(180deg,#c9a27f 0%,#e8c9ad 30%,#bcd0e4 55%,#9fb9d6 100%)}
.nav{position:absolute;top:22px;left:164px;right:164px;height:36px}
.brand{position:absolute;left:0;top:4px;display:flex;align-items:center;gap:8px;font-weight:700;font-size:18px;color:var(--blue-dark)}
.brand i{width:22px;height:22px;background:var(--blue);border-radius:50%;display:block}
.menu{position:absolute;right:0;top:8px;display:flex;gap:22px;font-size:12.5px;color:#333}
.hero-title{position:absolute;left:166px;top:200px;font-size:42px;font-weight:700;color:var(--blue)}
.hero-sub{position:absolute;left:166px;top:252px;font-size:30px;font-weight:300;color:#2b2f36}
.hero-line{position:absolute;left:166px;top:305px;font-size:15px;color:#3a3f46}
.btn{position:absolute;display:flex;align-items:center;justify-content:center;color:#fff;font-weight:700;font-size:12.5px;letter-spacing:.4px}
.btn-green{background:var(--green)}
.btn-blue{background:var(--blue)}

.h2{position:absolute;width:1200px;left:0;text-align:center;font-size:23px;font-weight:700;color:var(--ink)}
.lead{position:absolute;width:1200px;left:0;text-align:center;font-size:13.5px;color:#555}
.feat-title{position:absolute;font-size:21px;font-weight:700;color:var(--ink)}
.feat-kicker{position:absolute;font-size:12px;font-weight:700;color:var(--ink)}
.feat-text{position:absolute;font-size:11.5px;line-height:18px;color:var(--body)}
.shot{position:absolute;background:linear-gradient(180deg,#ffffff 0%,#eef3f8 100%);border:1px solid var(--line);box-shadow:0 4px 14px rgba(0,0,0,.08)}
.art{position:absolute;border-radius:12px}
.icon{position:absolute}
.product-name{position:absolute;font-size:22px;font-weight:700;color:var(--ink)}

.band{position:absolute;left:0;width:1200px;background:linear-gradient(100deg,#1a8fd8 0%,#3fb1ea 60%,#1a86cf 100%)}

.why-title{position:absolute;font-size:16px;font-weight:700;color:var(--ink)}
.why-text{position:absolute;font-size:11.5px;line-height:15px;color:var(--body);width:280px}

.testi{position:absolute;left:0;top:3483px;width:1200px;height:540px;background:var(--light)}
.card{position:absolute;background:#fff;text-align:center;font-style:italic;font-size:11.5px;line-height:18px;color:#666;padding:38px 22px 0}
.quote{position:absolute;width:34px;height:34px;border-radius:50%;display:flex;align-items:center;justify-content:center;color:#fff;font-weight:700;font-size:20px;font-style:normal}
.avatar{position:absolute;width:74px;height:74px;border-radius:50%;background:linear-gradient(180deg,#8c6a55 0%,#d9b59a 60%,#5a6b7c 100%);border:3px solid #fff}
.person{position:absolute;text-align:center;width:240px}
.person b{display:block;font-size:12.5px;font-weight:400;color:var(--ink)}
.person span{display:block;font-size:11px;font-style:italic;color:var(--muted);margin-top:6px}

.client{position:absolute;top:4180px;height:40px;display:flex;align-items:center;gap:8px;font-size:22px;font-weight:500;color:#3a4550}
.client i{width:14px;height:14px;border-radius:50%;background:var(--blue);display:block}
.arrow{position:absolute;top:4186px;width:30px;height:30px;border-radius:50%;background:#e4e6e9;display:flex;align-items:center;justify-content:center;color:#fff;font-size:14px}

.cta{position:absolute;left:0;top:4269px;width:1200px;height:138px;background:linear-gradient(100deg,#5cb84a 0%,#2fa3b8 45%,#1d86d0 100%)}

.footer{position:absolute;left:0;top:4407px;width:1200px;height:467px;background:var(--footer);color:var(--footer-text);font-size:10.5px;line-height:16px}
.fcol{position:absolute;top:42px}
.fcol h4{font-size:12px;font-weight:500;color:#fff;letter-spacing:.3px;padding-bottom:6px;border-bottom:2px solid var(--blue);display:inline-block;margin-bottom:12px}
.fcol p{margin-bottom:8px}
.fcol .hl{color:var(--blue)}
</style>
</head>
<body>

<header class="hero">
  <div class="hero-city" role="img" aria-label="Soft city skyline in the background"></div>
  <div class="hero-person" role="img" aria-label="Smiling support agent wearing a headset"></div>
  <nav class="nav">
    <div class="brand"><i></i>Harbor Zentrik</div>
    <div class="menu"><span>Home</span><span>Voice ▾</span><span>Data</span><span>Hardware ▾</span><span>Services Request ▾</span><span>Terms &amp; Conditions ▾</span><span>Status</span></div>
  </nav>
  <h1 class="hero-title">White-Label Solution</h1>
  <p class="hero-sub">for all your Communication Needs</p>
  <p class="hero-line">Liberating Businesses from Traditional Communications Systems</p>
  <a class="btn btn-green" style="left:168px;top:353px;width:156px;height:42px">LEARN MORE</a>
  <a class="btn btn-blue" style="left:336px;top:353px;width:156px;height:42px">REQUEST DEMO</a>
</header>

<h2 class="h2" style="top:650px">What We Offer</h2>
<p class="lead" style="top:700px">We have all the components to start and run your own White Label Telco</p>

<svg class="icon" style="left:176px;top:762px" width="48" height="44" viewBox="0 0 48 44" fill="none" stroke="#1a2f4a" stroke-width="2"><circle cx="24" cy="22" r="8"/><circle cx="6" cy="8" r="4"/><circle cx="42" cy="8" r="4"/><circle cx="6" cy="36" r="4"/><circle cx="42" cy="36" r="4"/><path d="M9 11l9 6M39 11l-9 6M9 33l9-6M39 33l-9-6"/></svg>
<h3 class="feat-title" style="left:177px;top:822px">Cloud IP PBX</h3>
<p class="feat-kicker" style="left:177px;top:857px">Multiple IP PBXs on a single instance</p>
<p class="feat-text" style="left:173px;top:890px;width:355px">A Multi-Tenant HarborPBX is able to handle multiple customers (tenants) with a single instance of the software. Even though every customer has a dedicated PBX, they all share the same switching core instance. Using the single instance for all customers cuts down operating costs significantly.</p>
<div class="art" style="left:805px;top:748px;width:190px;height:70px;border-radius:40px 40px 10px 10px;background:linear-gradient(90deg,#5fb8ea 0%,#a9adb3 100%)" role="img" aria-label="Blue and grey cloud graphic"></div>
<div class="shot" style="left:575px;top:818px;width:425px;height:155px" role="img" aria-label="System dashboard screenshot with tenant statistics"></div>

<div class="shot" style="left:180px;top:1107px;width:420px;height:250px" role="img" aria-label="Desktop and mobile communicator app screens"></div>
<div class="art" style="left:205px;top:1335px;width:170px;height:52px;border-radius:10px 10px 40px 40px;background:linear-gradient(90deg,#5fb8ea 0%,#a9adb3 100%)" role="img" aria-label="Blue and grey cloud graphic"></div>
<svg class="icon" style="left:664px;top:1110px" width="48" height="40" viewBox="0 0 48 40" fill="none" stroke="#1a2f4a" stroke-width="2"><path d="M12 32a9 9 0 0 1 0-18 13 13 0 0 1 25 2 8 8 0 0 1-1 16z"/><path d="M16 21h16l-4-4M32 26H16l4 4"/></svg>
<h3 class="feat-title" style="left:664px;top:1172px">Unified Communications</h3>
<p class="feat-kicker" style="left:669px;top:1214px">Available on Desktop &amp; Mobile</p>
<p class="feat-text" style="left:669px;top:1244px;width:365px">Communicator is a Desktop &amp; Mobile Unified Communications application designed to provide business users with a set of features and benefits capable of transforming your company communications system into a real powerhouse.</p>
<p class="feat-text" style="left:669px;top:1333px;width:365px">It is available on Fenestra Desktop, Macro OS, Ubiq Linux and on Andros and Pomme OS as a mobile application.</p>

<svg class="icon" style="left:176px;top:1545px" width="64" height="44" viewBox="0 0 64 44" fill="none" stroke="#1a2f4a" stroke-width="2"><rect x="2" y="20" width="30" height="20"/><path d="M2 26h30M6 34h10"/><rect x="28" y="4" width="26" height="32"/><path d="M33 12h16M33 18h16M33 24h10"/><text x="46" y="30" font-size="9" fill="#1e9be0" stroke="none">$</text></svg>
<h3 class="feat-title" style="left:173px;top:1610px">Invoice &amp; Payment Platform</h3>
<p class="feat-kicker" style="left:173px;top:1645px">All pieces in one for an assertive management</p>
<p class="feat-text" style="left:173px;top:1677px;width:355px">Access Portal is a fully-featured telecom customer portal, designed for integration with one or many HarborPBX telephony switches. Access Portal has a friendly GUI that enables efficient, automated billing, invoicing and payments, allowing you to spend less time dealing with the administration of your company and more time to SELL!</p>
<div class="art" style="left:840px;top:1520px;width:185px;height:62px;border-radius:40px 40px 10px 10px;background:linear-gradient(90deg,#5fb8ea 0%,#a9adb3 100%)" role="img" aria-label="Blue and grey cloud graphic"></div>
<div class="product-name" style="left:602px;top:1548px">Zentrik UC</div>
<div class="shot" style="left:596px;top:1582px;width:430px;height:236px" role="img" aria-label="Access portal dashboard with call statistics"></div>

<div class="art" style="left:190px;top:1884px;width:326px;height:346px;background:linear-gradient(180deg,#7cc7ef 0%,#c3c6ca 35%,#eef2f5 60%,#e3e8ec 100%)" role="img" aria-label="Illustration of a cloud streaming data to laptop, desktop and phone"></div>
<svg class="icon" style="left:664px;top:1904px" width="30" height="44" viewBox="0 0 30 44" fill="none" stroke="#1a2f4a" stroke-width="2"><path d="M7 20a6 6 0 0 1 0-12 9 9 0 0 1 17 2 5 5 0 0 1-1 10"/><rect x="10" y="16" width="11" height="24" rx="2"/><path d="M15.5 22v10M12 28l3.5 4 3.5-4"/></svg>
<h3 class="feat-title" style="left:664px;top:1974px">Data Services</h3>
<p class="feat-text" style="left:667px;top:2018px;width:380px"><b style="color:var(--ink)">Data Networks</b> <span style="font-size:10px">* not all services available all areas</span></p>
<p class="feat-text" style="left:667px;top:2052px"><b style="color:var(--ink)">Fibre</b></p>
<p class="feat-text" style="left:667px;top:2089px;width:380px"><b style="color:var(--ink)">Ethernet</b> – Symmetrical upload and downloads</p>
<p class="feat-text" style="left:667px;top:2126px;width:340px"><b style="color:var(--ink)">Wideband</b> – choose from three Internet speeds all with unlimited downloads</p>

<svg class="icon" style="left:172px;top:2324px" width="62" height="50" viewBox="0 0 62 50" fill="none" stroke="#1a2f4a" stroke-width="2"><circle cx="31" cy="24" r="13"/><circle cx="31" cy="24" r="5"/><path d="M13 24a18 18 0 0 1 36 0"/><rect x="8" y="22" width="6" height="12" rx="2"/><rect x="48" y="22" width="6" height="12" rx="2"/></svg>
<h3 class="feat-title" style="left:173px;top:2394px">Voice Services</h3>
<p class="feat-kicker" style="left:173px;top:2430px">Lorem ipsum dolor sit amet</p>
<p class="feat-text" style="left:173px;top:2460px;width:360px">Everything for your Business Communications<br>Inbound Services, Call Termination, 1300 &amp; 1800 Services<br>Phone Number, Number Porting, Virtual Fax<br>Sip Trunk and Connectivity, SMS, Conference Bridge</p>
<div class="art" style="left:662px;top:2328px;width:256px;height:248px;border-radius:50%;background:radial-gradient(circle,#8ccbee 0%,#c8ccd1 45%,#f2f5f8 72%,#ffffff 100%)" role="img" aria-label="Illustration of a cloud linking phones, a headset agent and a tablet"></div>

<section class="band" style="top:2658px;height:138px">
  <h3 class="abs" style="left:236px;top:26px;font-size:25px;font-weight:700;color:#fff">Support</h3>
  <p class="abs" style="left:234px;top:64px;width:520px;font-size:15px;line-height:21px;color:#e6f4fc">Our technical support team is always available to you via phone, live chat and support ticketing system.</p>
  <a class="btn btn-green" style="left:806px;top:50px;width:168px;height:42px">GET SUPPORT</a>
</section>

<h2 class="h2" style="top:2843px">Why Choose <span style="color:var(--blue)">Harbor</span> Zentrik</h2>
<p class="lead" style="top:2900px">Aenean ultricies dapibus justo, id ultricies magna eleifend nec. Integer magna magna, mollis eu quam nec.</p>

<svg class="icon" style="left:360px;top:2957px" width="76" height="52" viewBox="0 0 76 52" fill="none" stroke="#1a2f4a" stroke-width="2"><rect x="2" y="2" width="72" height="44"/><path d="M10 12h40M10 20h40M10 28h30M10 36h30"/><circle cx="62" cy="32" r="7" stroke="#1e9be0"/></svg>
<p class="why-title" style="left:355px;top:3030px">Experience</p>
<p class="why-text" style="left:166px;top:3056px;text-align:center">Lorem ipsum dolor sit amet, consectetur adipiscing elit. Sed elementum justo eu metus imperdiet, vestibulum cursus magna imperdiet.</p>

<svg class="icon" style="left:758px;top:2953px" width="70" height="60" viewBox="0 0 70 60" fill="none" stroke="#1a2f4a" stroke-width="2"><path d="M14 10a22 22 0 1 0 10 -6"/><path d="M14 2v9h9"/><path d="M36 52h28l-6-6M64 52l-6 6" stroke="#1e9be0"/></svg>
<p class="why-title" style="left:758px;top:3030px">Flexibility</p>
<p class="why-text" style="left:758px;top:3056px">Lorem ipsum dolor sit amet, consectetur adipiscing elit. Sed elementum justo eu metus imperdiet, vestibulum cursus magna imperdiet.</p>

<div class="art" style="left:496px;top:3057px;width:202px;height:142px;border-radius:70px 70px 40px 40px;background:linear-gradient(90deg,#1378c6 0%,#3fb1ea 45%,#c9ccd1 60%,#8d9298 100%)" role="img" aria-label="Glossy blue and silver cloud graphic"></div>

<svg class="icon" style="left:380px;top:3180px" width="56" height="74" viewBox="0 0 56 74" fill="none" stroke="#1a2f4a" stroke-width="2"><path d="M30 2c-10 8-16 18-12 28l16 12c4 10-6 18-16 20"/><path d="M6 66h44" stroke="#1e9be0"/><path d="M34 4l8 8"/></svg>
<p class="why-title" style="left:177px;top:3256px">Solutions tailored for your business</p>
<p class="why-text" style="left:166px;top:3283px;text-align:center">Lorem ipsum dolor sit amet, consectetur adipiscing elit. Sed elementum justo eu metus imperdiet, vestibulum cursus magna imperdiet.</p>

<svg class="icon" style="left:756px;top:3176px" width="76" height="72" viewBox="0 0 76 72" fill="none" stroke="#1a2f4a" stroke-width="2"><rect x="4" y="4" width="56" height="44" rx="4"/><circle cx="32" cy="26" r="10" stroke="#1e9be0"/><circle cx="32" cy="26" r="4" stroke="#1e9be0"/><path d="M60 20h12v40l-8-8H40v-4"/></svg>
<p class="why-title" style="left:758px;top:3256px">Support</p>
<p class="why-text" style="left:758px;top:3283px">Lorem ipsum dolor sit amet, consectetur adipiscing elit. Sed elementum justo eu metus imperdiet, vestibulum cursus magna imperdiet.</p>

<a class="btn btn-blue" style="left:517px;top:3379px;width:166px;height:42px">FREE TRIAL</a>

<section class="testi">
  <h2 class="h2" style="top:40px">Testimonials</h2>
  <p class="lead" style="top:80px;font-size:13px">What They Say About Harbor Zentrik</p>

  <div class="card" style="left:165px;top:161px;width:270px;height:176px">Lorem ipsum dolor sit amet, consectetur adipiscing elit. In iaculis, dolor sit amet tristique ornare, elit dolor maximus diam, ut hendrerit eros massa posuere velit.</div>
  <div class="quote" style="left:283px;top:144px;background:var(--blue)">”</div>
  <div class="avatar" style="left:262px;top:316px" role="img" aria-label="Portrait of Marcus Delaine"></div>
  <div class="person" style="left:180px;top:410px"><b>MARCUS DELAINE</b><span>Lorem ipsum dolor</span></div>

  <div class="card" style="left:464px;top:161px;width:270px;height:208px">Lorem ipsum dolor sit amet, consectetur adipiscing elit. In iaculis, dolor sit amet tristique ornare, elit dolor maximus diam, ut hendrerit eros massa posuere velit. Lorem ipsum dolor sit amet, consectetur adipiscing elit.</div>
  <div class="quote" style="left:582px;top:144px;background:var(--green)">”</div>
  <div class="avatar" style="left:562px;top:348px" role="img" aria-label="Portrait of Tobias Krenn"></div>
  <div class="person" style="left:479px;top:436px"><b>TOBIAS KRENN</b><span>Lorem ipsum dolor</span></div>

  <div class="card" style="left:763px;top:161px;width:274px;height:176px">Lorem ipsum dolor sit amet, consectetur adipiscing elit. In iaculis, dolor sit amet tristique ornare, elit dolor maximus diam, ut hendrerit eros massa posuere velit.</div>
  <div class="quote" style="left:883px;top:144px;background:var(--blue)">”</div>
  <div class="avatar" style="left:862px;top:316px" role="img" aria-label="Portrait of Felix Aranda"></div>
  <div class="person" style="left:780px;top:410px"><b>FELIX ARANDA</b><span>Lorem ipsum dolor</span></div>
</section>

<h2 class="h2" style="top:4077px">Our Clients</h2>
<div class="arrow" style="left:122px">‹</div>
<div class="client" style="left:170px"><i></i>Norvale</div>
<div class="client" style="left:352px"><i></i>Quillstone</div>
<div class="client" style="left:538px"><i></i>Tarvik</div>
<div class="client" style="left:702px"><i></i>Brightmoor</div>
<div class="client" style="left:870px"><i></i>Olvera</div>
<div class="arrow" style="left:1046px">›</div>

<section class="cta">
  <p class="abs" style="left:268px;top:58px;font-size:16px;font-weight:300;color:#fff">Lorem ipsum dolor sit amet, consectetur adipiscing elit.</p>
  <a class="btn" style="left:732px;top:48px;width:196px;height:42px;background:var(--blue-dark);font-size:15px;gap:10px">
    <svg width="16" height="16" viewBox="0 0 16 16" fill="none" stroke="#fff" stroke-width="2"><circle cx="8" cy="8" r="7"/><path d="M4.5 8l2.5 2.5 4.5-5"/></svg>FREE TRIAL</a>
</section>

<footer class="footer">
  <div class="fcol" style="left:161px;width:200px">
    <h4>ABOUT US</h4>
    <div style="width:64px;height:36px;margin:8px 0 14px;border-radius:18px;background:linear-gradient(90deg,#3fb1ea 0%,#b9bcc1 100%)" role="img" aria-label="Harbor Zentrik cloud emblem"></div>
    <p><span class="hl">Harbor Zentrik</span> - Lorem ipsum dolor sit amet, consectetur adipiscing elit. Integer interdum aliquam diam, id sodales enim volutpat sit amet. Sed nec mi risus. Ut eu turpis ac enim vestibulum scelerisque.</p>
    <p class="hl">More</p>
  </div>
  <div class="fcol" style="left:413px">
    <h4>INFORMATION</h4>
    <p>Products</p><p>Terms of Service</p><p>Privacy Policy</p><p>Sitemap</p><p>About</p><p>Contact</p>
  </div>
  <div class="fcol" style="left:598px;width:200px">
    <h4>CONTACT INFO</h4>
    <p><span class="hl">Administration</span><br>admin@harborzentrik.com.au<br>+61200000101</p>
    <p><span class="hl">Accounts</span><br>accounts@harborzentrik.com.au<br>+61200000101</p>
    <p><span class="hl">Support</span><br>support@harborzentrik.com.au<br>+61200000102</p>
    <p style="padding-left:22px;margin-top:14px;position:relative"><svg style="position:absolute;left:4px;top:2px" width="10" height="14" viewBox="0 0 10 14" fill="#1e9be0"><path d="M5 0a5 5 0 0 1 5 5c0 4-5 9-5 9S0 9 0 5a5 5 0 0 1 5-5z"/><circle cx="5" cy="5" r="2" fill="#1d2733"/></svg>ABN 00 000 000 000<br>PO Box 1200<br>Eastwharf ACT 2900</p>
  </div>
  <div class="fcol" style="left:846px">
    <h4>SOCIAL</h4>
    <p><span class="hl">■</span>&nbsp; Friendwall</p><p><span class="hl">■</span>&nbsp; Careerlink</p><p><span class="hl">■</span>&nbsp; Circle Plus</p><p><span class="hl">■</span>&nbsp; Chirpfeed</p>
  </div>
  <p class="abs" style="left:161px;top:344px">© harborzentrik.com.au 2019</p>
  <div class="abs" style="left:1008px;top:342px;width:24px;height:24px;border-radius:50%;border:1px solid #3d4956;color:#5f6b78;display:flex;align-items:center;justify-content:center;font-size:11px">⌃</div>
  <div class="abs" style="left:1044px;top:318px;width:34px;height:34px;border-radius:4px;background:var(--blue-dark);display:flex;align-items:center;justify-content:center">
    <svg width="18" height="16" viewBox="0 0 18 16" fill="none" stroke="#fff" stroke-width="1.6"><rect x="1" y="1" width="11" height="8" rx="1"/><path d="M6 11v2h7l3 2v-9h-3"/></svg>
  </div>
</footer>

</body>
</html>
```